CREATIVE DESIGNERS NEEDED & Enhance Your Business Card Portfolio

Artistic, unique, professional real estate card needed - see attached documents "B-cards.pdf" for all details and examples.True Designers will see other projects of ours come online here. We like long-term relationships for creative designers. This business card will be used in two U.S. states and is central to our business and other future marketing.

Target Market(s)

Buyers and Sellers of real estate

Industry/Entity Type

Real Estate Agent

Contact Information for Business Card

See attached detailed brief

Other font styles liked:
• ADAM.CG PRO & NewsGoth BT

Requirements
Must have
• 2-sided, creative (non-traditional layout/design). Incorporate a cut-out (for texture, and make it fun! No boring templates for this card -
Nice to have
• See attached detailed brief
Should not have

```html
<!DOCTYPE html>
<html lang="en">
<head>
<meta charset="UTF-8">
<title>Owen Hartley – Broker Associate &amp; Realtor</title>
<link rel="stylesheet" href="https://fonts.googleapis.com/css2?family=Lato:wght@700&display=swap">
<style>
  :root {
    --sky-violet: #363152;
    --sky-rose: #6a3d5e;
    --navy: #252c45;
    --facade: #2f3550;
    --navy-deep: #1a2033;
    --road: #1c2236;
    --foliage: #1b2a2c;
    --text-white: #ffffff;
  }
  html, body {
    margin: 0;
    padding: 0;
    width: 1200px;
    height: 720px;
    overflow: hidden;
    background: var(--navy-deep);
  }
  .card {
    position: relative;
    width: 1200px;
    height: 720px;
    overflow: hidden;
    font-family: "Lato", Arial, sans-serif;
    color: var(--text-white);
  }
  .card__backdrop {
    position: absolute;
    inset: 0;
    background:
      radial-gradient(ellipse 420px 90px at 160px 150px, rgba(106, 61, 94, 0.8), rgba(106, 61, 94, 0) 75%),
      radial-gradient(ellipse 300px 70px at 880px 80px, rgba(106, 61, 94, 0.45), rgba(106, 61, 94, 0) 75%),
      radial-gradient(ellipse 620px 170px at 600px 320px, rgba(70, 78, 110, 0.55), rgba(70, 78, 110, 0) 75%),
      radial-gradient(ellipse 260px 140px at 1120px 560px, rgba(27, 42, 44, 0.9), rgba(27, 42, 44, 0) 75%),
      linear-gradient(180deg,
        var(--sky-violet) 0%,
        var(--navy) 22%,
        var(--facade) 36%,
        var(--navy) 58%,
        var(--road) 72%,
        var(--navy-deep) 100%);
  }
  .brand {
    position: absolute;
    left: 469px;
    top: 210px;
    display: flex;
    align-items: center;
    gap: 16px;
    text-shadow: 0 1px 4px rgba(0, 0, 0, 0.35);
  }
  .brand__mark {
    width: 96px;
    height: 96px;
    border: 7px solid var(--text-white);
    box-sizing: border-box;
  }
  .brand__name {
    display: flex;
    flex-direction: column;
    font-weight: 700;
    text-transform: uppercase;
    line-height: 1;
  }
  .brand__name-main { font-size: 44px; letter-spacing: 0; }
  .brand__name-sub { font-size: 19px; margin-top: 6px; }
  .brand__name-tag { font-size: 13px; letter-spacing: 5.4px; margin-top: 5px; }
  .agent {
    position: absolute;
    left: 0;
    right: 0;
    top: 455px;
    text-align: center;
    text-shadow: 0 2px 6px rgba(0, 0, 0, 0.35);
  }
  .agent__name {
    margin: 0;
    font-weight: 700;
    font-size: 68px;
    line-height: 1;
    letter-spacing: 1px;
    text-transform: uppercase;
  }
  .agent__title {
    margin: 32px 0 0;
    font-weight: 700;
    font-size: 36px;
    line-height: 1;
    letter-spacing: 0.5px;
    text-transform: uppercase;
  }
</style>
</head>
<body>
  <main class="card">
    <div class="card__backdrop" role="img" aria-label="Dusk photograph of a row of modern three-storey townhouses with palm trees, a parked car and a curving street, under a dark navy overlay"></div>

    <div class="brand">
      <span class="brand__mark"></span>
      <span class="brand__name">
        <span class="brand__name-main">Hartley</span>
        <span class="brand__name-sub">Hartley Group</span>
        <span class="brand__name-tag">Real Estate</span>
      </span>
    </div>

    <section class="agent">
      <h1 class="agent__name">Owen Hartley</h1>
      <p class="agent__title">Broker Associate &amp; Realtor</p>
    </section>
  </main>
</body>
</html>
```